One of a kind service business!

We are the only ocean freight auditing company in the entire world that does what we do. We provide a innovative service in auditing our clients invoices for billing errors as it relates to the import and export of their products anywhere in the world. We'd like to retain the current logo - but we are open to any interesting concepts that can complete the card.

Target Market(s)

C-Level and Senior Financial executives

Industry/Entity Type

Auditing

Requirements
Must have

• ONE SIDED ONLY
Should not have
• no cartoonish images

```html
<!DOCTYPE html>
<html lang="en">
<head>
<meta charset="utf-8">
<title>Tidewell Audit — Business Card</title>
<link rel="stylesheet" href="https://fonts.googleapis.com/css2?family=Questrial&family=Poppins:wght@600&display=swap">
<style>
  :root {
    --page-bg: #e9e7e4;
    --card-dark: #3b3b3d;
    --card-light: #ffffff;
    --ink: #2b2b2d;
    --ink-soft: #6d6d70;
    --ink-faint: #9a9a9d;
    --brand-blue: #2a9fd6;
    --brand-white: #ffffff;
  }
  * { box-sizing: border-box; margin: 0; padding: 0; }
  html, body {
    width: 1200px;
    height: 897px;
    overflow: hidden;
    background: var(--page-bg);
  }
  .canvas {
    position: relative;
    width: 1200px;
    height: 897px;
  }
  .card {
    position: absolute;
    left: 100px;
    top: 131px;
    width: 1000px;
    height: 634px;
    background: var(--card-dark);
    box-shadow: 0 12px 30px rgba(0, 0, 0, 0.18);
  }
  .brand {
    position: absolute;
    left: 64px;
    top: 284px;
    display: flex;
    align-items: center;
    gap: 16px;
  }
  .brand-square {
    width: 40px;
    height: 40px;
    background: var(--brand-blue);
  }
  .brand-name {
    font-family: "Questrial", sans-serif;
    font-size: 44px;
    color: var(--brand-white);
    letter-spacing: 0.5px;
    line-height: 1;
  }
  .info-panel {
    position: absolute;
    left: 470px;
    top: 152px;
    width: 530px;
    height: 482px;
    background: var(--card-light);
  }
  .person-name {
    position: absolute;
    left: 26px;
    top: 20px;
    font-family: "Poppins", sans-serif;
    font-weight: 600;
    font-size: 36px;
    color: var(--ink);
    letter-spacing: 0.5px;
  }
  .person-title {
    position: absolute;
    left: 260px;
    top: 74px;
    font-family: "Questrial", sans-serif;
    font-size: 24px;
    color: var(--ink-faint);
    letter-spacing: 1px;
  }
  .contact {
    position: absolute;
    left: 26px;
    top: 180px;
    list-style: none;
    font-family: "Questrial", sans-serif;
    font-size: 25px;
    line-height: 31px;
    color: var(--ink-soft);
    letter-spacing: 0.6px;
  }
  .contact-label {
    color: var(--ink);
    font-weight: 700;
  }
</style>
</head>
<body>
<main class="canvas">
  <article class="card">
    <div class="brand">
      <span class="brand-square"></span>
      <span class="brand-name">Tidewell Audit</span>
    </div>
    <section class="info-panel">
      <h1 class="person-name">Marek Holloway</h1>
      <p class="person-title">CEO</p>
      <ul class="contact">
        <li>Riverside Plaza, Dlouha 18</li>
        <li>Prague - Czech Republic 110 00</li>
        <li><span class="contact-label">p</span> : +420 555 014 270</li>
        <li><span class="contact-label">m</span> : +420 555 019 384</li>
        <li><span class="contact-label">USA</span> : +1 555 013 6624</li>
        <li><span class="contact-label">f</span> : +420 555 017 412</li>
        <li><span class="contact-label">e</span> : MarekH@tidewellaudit.net</li>
        <li><span class="contact-label">w</span> : www.tidewellaudit.net</li>
      </ul>
    </section>
  </article>
</main>
</body>
</html>
```